Indy Film Production Company/Studio

We need a business card designed from an existing logo. We are a digital studio/production company that caters to creating genre entertainment, like Action, Horror, and martial arts. The card along with the logo will be used to Brand the company from letter heads to banners. The design will also be used for postcards and Brochures. It should be professional and masculine.
Updates

Thank you to all the designers who have participated. I'm narrowing down who it will be. Thank you again.

Target Market(s)

Investors, Networks, Producers, and actors

Industry/Entity Type

Film Production

Contact Information for Business Card

Benedict Harlowe
Producer/Writer/Director
www.pelvarmotionworks.com

Requirements
Must have
• Website address, Facebook icon and Twitter icon possibly in the back of the card.
Nice to have
• Logline of Company: Follow The Action.

```html
<!DOCTYPE html>
<html lang="en">
<head>
<meta charset="utf-8">
<title>Pelvar Motion Works – Business Card</title>
<link href="https://fonts.googleapis.com/css2?family=Khand:wght@600&family=Roboto:wght@400&display=swap" rel="stylesheet">
<style>
  :root {
    --backdrop: #a9a7a7;
    --card: #f1f1f0;
    --brand-red: #c8302b;
    --band-red: #bf2e27;
    --band-edge: #a8261f;
    --ink: #1d1d1d;
  }
  html, body {
    margin: 0;
    width: 1200px;
    height: 1200px;
    overflow: hidden;
    background: var(--backdrop);
  }
  .canvas {
    position: relative;
    width: 1200px;
    height: 1200px;
  }
  .card {
    position: absolute;
    width: 712px;
    height: 418px;
    background: var(--card);
  }
  .card--front { left: 238px; top: 119px; }
  .card--back  { left: 231px; top: 644px; }

  .wordmark {
    position: absolute;
    display: flex;
    align-items: center;
    gap: 14px;
    font-family: "Khand", sans-serif;
    font-weight: 600;
    color: var(--brand-red);
    text-transform: uppercase;
    line-height: 1;
    white-space: nowrap;
  }
  .wordmark__square {
    display: block;
    background: var(--brand-red);
  }
  .card--front .wordmark {
    left: 0; right: 0;
    top: 180px;
    justify-content: center;
    font-size: 50px;
  }
  .card--front .wordmark__square { width: 34px; height: 34px; }
  .card--back .wordmark {
    right: 55px;
    top: 80px;
    font-size: 34px;
    gap: 10px;
  }
  .card--back .wordmark__square { width: 24px; height: 24px; }

  .accent-band {
    position: absolute;
    left: 0; top: 0;
    width: 60px; height: 100%;
    background: var(--band-red);
    border-right: 8px solid var(--band-edge);
  }
  .person {
    position: absolute;
    left: 95px;
    top: 176px;
  }
  .person__name {
    margin: 0;
    font-family: "Khand", sans-serif;
    font-weight: 600;
    font-size: 29px;
    color: var(--ink);
    line-height: 1;
  }
  .person__role {
    margin: 12px 0 0;
    font-family: "Roboto", sans-serif;
    font-size: 16px;
    color: var(--brand-red);
  }
  .contacts {
    position: absolute;
    left: 95px;
    top: 272px;
    margin: 0;
    padding: 0;
    list-style: none;
    font-family: "Roboto", sans-serif;
    font-size: 18px;
    color: var(--ink);
  }
  .contacts__item {
    display: flex;
    align-items: center;
    height: 28px;
  }
  .contacts__icon {
    width: 14px;
    height: 14px;
    margin: 0 21px 0 1px;
    fill: var(--brand-red);
  }
  .contacts__address { margin-top: 4px; }
</style>
</head>
<body>
<div class="canvas">

  <section class="card card--front">
    <div class="wordmark">
      <span class="wordmark__square"></span>
      <span class="wordmark__name">Pelvar Motion Works</span>
    </div>
  </section>

  <section class="card card--back">
    <div class="accent-band"></div>

    <div class="wordmark">
      <span class="wordmark__square"></span>
      <span class="wordmark__name">Pelvar Motion Works</span>
    </div>

    <div class="person">
      <p class="person__name">Your Good Name</p>
      <p class="person__role">Managing Director</p>
    </div>

    <ul class="contacts">
      <li class="contacts__item">
        <svg class="contacts__icon" viewBox="0 0 16 16" aria-hidden="true">
          <path d="M1 5c0-2 3-3 7-3s7 1 7 3v1h-3V5H4v1H1z"/>
          <path d="M3 7h10l1 7H2z"/>
        </svg>
        +00 111 222 3333
      </li>
      <li class="contacts__item">
        <svg class="contacts__icon" viewBox="0 0 16 16" aria-hidden="true">
          <path d="M1 3h14v10H1z M2 4l6 5 6-5" fill="var(--brand-red)"/>
          <path d="M2 4l6 5 6-5" fill="none" stroke="#f1f1f0" stroke-width="1.3"/>
        </svg>
        yourname@yourwebsite.com
      </li>
      <li class="contacts__item">
        <svg class="contacts__icon" viewBox="0 0 16 16" aria-hidden="true">
          <circle cx="8" cy="8" r="7"/>
          <path d="M1 8h14M8 1v14M3 4h10M3 12h10" stroke="#f1f1f0" stroke-width="1" fill="none"/>
          <ellipse cx="8" cy="8" rx="3" ry="7" fill="none" stroke="#f1f1f0" stroke-width="1"/>
        </svg>
        www.yourwebsite.com
      </li>
      <li class="contacts__item contacts__address">Your Long Commercial or business&nbsp; address in 2 line</li>
    </ul>
  </section>

</div>
</body>
</html>
```